Marlow Nightclub Flyer Grand Opening

Grand Opening Teaser Flyer For Nightclub

Text for flyer:
MARLOW
Nightclub + Lounge
Opening Fall 2018
Downtown Sacramento
Now Hiring (All Positions)
www.marlowvenue-example.com
Powered by KELP Acoustics

Email Resume to: club@marlowvenue-example.com

Target Market(s)

Upscale Nightclub and Lounge

Industry/Entity Type

Night Club

Font styles to use
Sans Serif

Colors
9ccb3b
0393ce
0355a3
b2b2b2
000000

Requirements
Must have
• Vibrant colors like the flyer example, and our logo. For use on Chatterly and Pictoria, will be boosted as well.
Nice to have
• Something artsy like the flyer example but not required

```html
<!DOCTYPE html>
<html lang="en">
<head>
<meta charset="utf-8">
<title>Marlow Nightclub + Lounge — Opening Fall 2018</title>
<link rel="stylesheet" href="https://fonts.googleapis.com/css2?family=Montserrat:wght@300;400;600;700&family=Quicksand:wght@500&display=swap">
<style>
  :root {
    --bg-deep: #081a1d;
    --bg-teal: #155a5e;
    --bg-petrol: #0d4756;
    --white: #ffffff;
    --mint: #20d39b;
    --navy-text: #0b2a4a;
    --slate-teal: #6a9ea6;
    --royal: #0f3c8e;
  }
  html, body {
    margin: 0;
    padding: 0;
    width: 1200px;
    height: 1200px;
    overflow: hidden;
    background: var(--bg-deep);
  }
  .flyer {
    position: relative;
    width: 1200px;
    height: 1200px;
    overflow: hidden;
  }
  .flyer__backdrop {
    position: absolute;
    inset: 0;
    background:
      radial-gradient(ellipse at 35% 40%, rgba(30, 110, 110, 0.55), transparent 60%),
      linear-gradient(135deg, var(--bg-petrol) 0%, var(--bg-teal) 45%, #0f3c3f 70%, var(--bg-deep) 100%);
  }
  .flyer__art {
    position: absolute;
    inset: 0;
  }
  .frame-line { stroke: var(--white); stroke-width: 3.5; fill: none; }
  .opening-box { stroke: var(--white); stroke-width: 3.5; fill: none; }
  .opening-text {
    font-family: "Montserrat", sans-serif;
    font-weight: 700;
    font-size: 26px;
    letter-spacing: 5px;
    fill: var(--white);
  }
  .venue-name {
    font-family: "Quicksand", sans-serif;
    font-weight: 500;
    font-size: 168px;
    fill: var(--white);
  }
  .venue-tagline {
    font-family: "Montserrat", sans-serif;
    font-weight: 300;
    font-size: 33px;
    fill: var(--white);
  }
  .info-heading {
    font-family: "Montserrat", sans-serif;
    font-weight: 700;
    font-size: 26px;
    fill: var(--white);
  }
  .web-band { fill: var(--mint); }
  .web-text {
    font-family: "Montserrat", sans-serif;
    font-weight: 700;
    font-size: 20px;
    fill: var(--navy-text);
  }
  .email-label-band { fill: var(--slate-teal); }
  .email-band { fill: var(--royal); }
  .email-text {
    font-family: "Montserrat", sans-serif;
    font-weight: 700;
    font-size: 19px;
    fill: var(--white);
  }
  .powered-text {
    font-family: "Montserrat", sans-serif;
    font-weight: 600;
    font-size: 14px;
    fill: var(--white);
  }
  .sound-partner {
    font-family: "Montserrat", sans-serif;
    font-weight: 700;
    font-size: 26px;
    fill: var(--white);
  }
</style>
</head>
<body>
  <main class="flyer">
    <div class="flyer__backdrop" role="img" aria-label="Dark teal background with faint faceted geometric triangles"></div>

    <svg class="flyer__art" width="1200" height="1200" viewBox="0 0 1200 1200" xmlns="http://www.w3.org/2000/svg">
      <!-- Frame -->
      <g class="frame">
        <line class="frame-line" x1="156" y1="157" x2="512" y2="157"/>
        <line class="frame-line" x1="689" y1="157" x2="1042" y2="157"/>
        <line class="frame-line" x1="157.5" y1="156" x2="157.5" y2="428"/>
        <line class="frame-line" x1="157.5" y1="592" x2="157.5" y2="1042"/>
        <line class="frame-line" x1="1040.5" y1="156" x2="1040.5" y2="428"/>
        <line class="frame-line" x1="1040.5" y1="592" x2="1040.5" y2="1042"/>
        <line class="frame-line" x1="156" y1="1040.5" x2="1042" y2="1040.5"/>
      </g>

      <!-- Opening date badge -->
      <g class="opening">
        <rect class="opening-box" x="513" y="101" width="175" height="202"/>
        <text class="opening-text" x="601" y="151" text-anchor="middle">OPE</text>
        <text class="opening-text" x="601" y="175" text-anchor="middle">NING</text>
        <text class="opening-text" x="601" y="220" text-anchor="middle">FALL</text>
        <text class="opening-text" x="601" y="266" text-anchor="middle">2018</text>
      </g>

      <!-- Venue name -->
      <text class="venue-name" x="74" y="546" textLength="1054" lengthAdjust="spacing">MARLOW</text>
      <text class="venue-tagline" x="214" y="602" textLength="776" lengthAdjust="spacing">NIGHTCLUB + LOUNGE</text>

      <!-- Location and website -->
      <text class="info-heading" x="340" y="764" textLength="522" lengthAdjust="spacing">DOWNTOWN SACRAMENTO</text>
      <polygon class="web-band" points="340,782 876,782 862,826 326,826"/>
      <text class="web-text" x="601" y="811" text-anchor="middle" letter-spacing="2.2">WWW.MARLOWVENUE-EXAMPLE.COM</text>

      <!-- Hiring -->
      <text class="info-heading" x="350" y="904" textLength="500" lengthAdjust="spacing">NOW HIRING (ALL POSITIONS)</text>
      <polygon class="email-label-band" points="234,919 500,919 488,958 222,958"/>
      <polygon class="email-band" points="500,919 982,919 970,958 488,958"/>
      <text class="email-text" x="361" y="945" text-anchor="middle" letter-spacing="2.5">EMAIL RESUME TO</text>
      <text class="email-text" x="731" y="945" text-anchor="middle" letter-spacing="1.6">CLUB@MARLOWVENUE-EXAMPLE.COM</text>

      <!-- Sound partner -->
      <text class="powered-text" x="274" y="1094" textLength="176" lengthAdjust="spacing">POWERED BY</text>
      <text class="sound-partner" x="600" y="1098" text-anchor="middle" letter-spacing="3">KELP</text>
      <text class="powered-text" x="700" y="1094" textLength="230" lengthAdjust="spacing">ACOUSTICS</text>
    </svg>
  </main>
</body>
</html>
```